Builders Worksite Corflute Outdoor Sign

We are a building company who are just branching out into new construction. How first new build is our own home which was designed by us and a local architect. We are proud and want to create more advertisement around our business.

We need a corflute sign that can staked outside the construction site and can be seen by people passing by.
Updates

Can we please make the company name and logo bigger (Tidewater Ridge Homes) This needs to be the focus. Can we please replace 'Manu' with 'Contact Us on 021-574-3619'

Target Market(s)

Home owners and people wishing to build on lifestyle blocks in New Zealand.

Font styles to use
Sans Serif

Requirements
Must have
• It needs to feature our:
Logo
Company name
Contact name and number - Manu - 0215743619
Landscape NOT portrait.

```html
<!DOCTYPE html>
<html lang="en">
<head>
<meta charset="utf-8">
<title>Tidewater Ridge Homes – Worksite Sign</title>
<link rel="stylesheet" href="https://fonts.googleapis.com/css2?family=Jost:wght@300;400&family=Montserrat:wght@700;800&display=swap">
<style>
  :root {
    --navy: #1c2235;
    --gold: #f0b323;
    --white: #ffffff;
    --silver: #d4d6da;
    --red: #e23b2e;
    --ink: #1c2235;
    --service-grey: #767b85;
    --backdrop: #e6e6e6;
  }
  * { box-sizing: border-box; margin: 0; padding: 0; }
  html, body { width: 787px; height: 1200px; overflow: hidden; }
  body { background: var(--backdrop); position: relative; }

  .sign {
    position: absolute; left: 60px; top: 342px;
    width: 666px; height: 516px;
    background: var(--navy);
    overflow: hidden;
    box-shadow: 0 10px 30px rgba(0,0,0,.25);
  }
  .sign-backdrop { position: absolute; inset: 0; }

  .brand-mark {
    position: absolute; left: 306px; top: 62px;
    width: 68px; height: 68px; border-radius: 50%;
    background: var(--gold);
  }
  .brand-name {
    position: absolute; left: 0; width: 100%; text-align: center;
    font-family: "Jost", sans-serif; font-weight: 400;
    color: var(--white); line-height: 1; white-space: nowrap;
  }
  .brand-name--main { top: 172px; font-size: 62px; letter-spacing: 0.5px; }
  .brand-name--sub { top: 250px; font-size: 33px; letter-spacing: 0.5em; padding-left: 0.5em; }

  .photo {
    position: absolute; border-radius: 50%;
    border: 4px solid var(--gold);
  }
  .photo--planning {
    left: 33px; top: 249px; width: 152px; height: 152px;
    background: linear-gradient(135deg, #c9a77a 0%, #d8d24a 45%, #6f7d8c 100%);
  }
  .photo--installing {
    left: 483px; top: 256px; width: 160px; height: 160px;
    background: linear-gradient(135deg, #f1f1f1 0%, #e4e7ec 45%, #3b5fa8 100%);
  }

  .seal {
    position: absolute; left: 288px; top: 296px;
    width: 114px; height: 114px; border-radius: 50%;
    background: var(--gold);
  }

  .contact-label {
    position: absolute; left: 88px; top: 408px;
    font-family: "Jost", sans-serif; font-weight: 300;
    font-size: 24px; color: var(--ink); line-height: 1;
    display: flex; align-items: center; gap: 6px;
  }
  .contact-label svg { width: 18px; height: 18px; }
  .contact-number {
    position: absolute; left: 33px; top: 431px;
    font-family: "Montserrat", sans-serif; font-weight: 800;
    font-size: 51px; letter-spacing: -0.5px; color: var(--ink); line-height: 1;
    white-space: nowrap;
  }
  .divider {
    position: absolute; left: 370px; top: 420px;
    width: 1px; height: 58px; background: var(--ink);
  }
  .cert-badge { position: absolute; left: 385px; top: 418px; width: 46px; height: 60px; }
  .cert-text {
    position: absolute; left: 441px; top: 430px;
    font-family: "Montserrat", sans-serif; font-weight: 700;
    font-size: 9.5px; line-height: 11.5px; color: var(--red);
  }
  .cert-text .cert-lead { color: var(--ink); }

  .services {
    position: absolute; left: 30px; right: 30px; top: 488px;
    display: flex; justify-content: space-between; align-items: center;
    font-family: "Montserrat", sans-serif; font-weight: 700;
    font-size: 13.4px; color: var(--service-grey); line-height: 1;
    list-style: none; white-space: nowrap;
  }
  .services li { display: flex; align-items: center; gap: 7px; }
  .services li::before {
    content: ""; width: 8px; height: 8px; border-radius: 50%;
    background: var(--gold);
  }
</style>
</head>
<body>
  <main class="sign">
    <svg class="sign-backdrop" viewBox="0 0 666 516" width="666" height="516" aria-hidden="true">
      <polygon points="0,391 154,323 447,401 666,482 666,516 0,516" fill="var(--white)"/>
      <polygon points="447,401 666,303 666,351" fill="var(--silver)"/>
      <polygon points="447,401 666,351 666,482" fill="var(--gold)"/>
    </svg>

    <div class="brand-mark" aria-hidden="true"></div>
    <h1 class="brand-name brand-name--main">TIDEWATER RIDGE</h1>
    <p class="brand-name brand-name--sub">HOMES</p>

    <div class="photo photo--planning" role="img" aria-label="Builders in hard hats and hi-vis vests reviewing plans on a timber-framed site"></div>
    <div class="photo photo--installing" role="img" aria-label="Tradesmen in blue overalls and yellow hard hats fitting out an interior wall"></div>

    <div class="seal" role="img" aria-label="Gold seal badge stating the team are registered professionals"></div>

    <p class="contact-label">
      <svg viewBox="0 0 20 20" aria-hidden="true">
        <circle cx="10" cy="10" r="8.5" fill="none" stroke="var(--ink)" stroke-width="1.6"/>
        <path d="M7 5.5l1.6 2.3-1 1c.6 1.3 1.6 2.3 2.9 2.9l1-1 2.3 1.6-.9 1.6c-3.4-.4-6.1-3.1-6.6-6.5z" fill="var(--ink)"/>
      </svg>
      CONTACT US ON
    </p>
    <p class="contact-number">021-574-3619</p>

    <div class="divider" aria-hidden="true"></div>
    <svg class="cert-badge" viewBox="0 0 46 60" aria-hidden="true">
      <path d="M0 0H46V46L23 60L0 46Z" fill="var(--red)"/>
    </svg>
    <p class="cert-text">
      <span class="cert-lead">CERTIFIED BY</span><br>
      KAURI BAY<br>
      CERTIFIED TRADES<br>
      GUILD
    </p>

    <ul class="services">
      <li>NEW HOMES</li>
      <li>EXTENSIONS</li>
      <li>REFURBISHMENTS</li>
      <li>GARAGE CONVERSIONS</li>
    </ul>
  </main>
</body>
</html>
```